Online Media Company Website

Looking for a website design that clearly and powerfully portrays our brand. Vantorell. We are an online media technology company that helps advertisers understand the content and verify the context where they advertise in online video.

You can see more about our company at www.vantorell-example.tv and watch the video. The only thing you must keep is the logo (attached). Everything else is fair game.

We need the following sections:

Home
About Us
-Company
-Careers
-Management
Technology
-Publisher Solutions
-Advertiser Solutions
Press
Contact Us

On the main page should be a space where we can place our video plus showcase some important news such as whitepapers..etc.

Please include social media functions on the homepage such as twitter/facebook. Perhaps a section for a twitter feed.

Sites we like:
www.pelvagrin-example.com
www.quibbenlark-example.com
www.haskomelt-example.com
www.dorvanteq-example.com

Industry/Entity Type

Tv

Requirements
Nice to have
• social media feed

```html
<!DOCTYPE html>
<html lang="en">
<head>
<meta charset="utf-8">
<title>Vantorell – Online Video Context</title>
<link rel="stylesheet" href="https://fonts.googleapis.com/css2?family=Arimo:ital,wght@0,400;0,700;1,400;1,700&display=swap">
<style>
  :root {
    --ink: #0e3a4f;
    --ink-soft: #1b4a60;
    --teal: #1b7f9a;
    --teal-dark: #0a5a72;
    --page: #e8e8e8;
    --page-light: #f4f4f4;
    --rule: #d2d2d2;
    --panel-border: #c9c9c9;
    --video-light: #2a8ae0;
    --video-dark: #0548b0;
    --thumb-light: #d8dfe2;
    --thumb-blue: #7fc2dc;
    --white: #ffffff;
  }
  * { box-sizing: border-box; margin: 0; padding: 0; }
  html, body { width: 1200px; height: 1040px; overflow: hidden; }
  body {
    position: relative;
    font-family: "Arimo", Arial, sans-serif;
    color: var(--ink);
    background: radial-gradient(ellipse at 50% 45%, var(--page-light) 0%, var(--page) 60%, #e2e2e2 100%);
  }

  /* Header */
  .site-header {
    position: absolute; left: 0; top: 0; width: 1200px; height: 66px;
    background: linear-gradient(#ffffff, #f1f1f1);
    border-bottom: 1px solid #c8c8c8;
    box-shadow: 0 1px 3px rgba(0,0,0,0.08);
  }
  .brand {
    position: absolute; left: 150px; top: 12px; height: 42px;
    display: flex; align-items: center; gap: 8px;
    color: var(--teal); font-size: 38px; font-weight: 400; letter-spacing: 1px;
  }
  .brand-dot { width: 34px; height: 34px; border-radius: 50%; background: var(--teal-dark); }
  .main-nav { position: absolute; left: 595px; top: 0; height: 65px; display: flex; }
  .main-nav a {
    display: block; height: 65px; line-height: 68px; padding: 0 22px;
    font-size: 13px; font-weight: 700; color: var(--ink); text-decoration: none;
  }
  .main-nav a.is-active {
    width: 80px; padding: 0; text-align: center; color: var(--white);
    background: linear-gradient(#0d6e88, #0a4e66);
  }

  /* Hero */
  .hero {
    position: absolute; left: 150px; top: 100px; width: 900px; height: 350px;
    background: radial-gradient(ellipse at 50% 55%, #f2f3f2 0%, #dcdedc 55%, #bfc2bf 100%);
    box-shadow: 0 1px 3px rgba(0,0,0,0.35);
  }

  /* Main content */
  .welcome-title {
    position: absolute; left: 150px; top: 469px; width: 580px; text-align: center;
    font-size: 25px; font-weight: 700; font-style: italic; color: var(--ink);
  }
  .feature { position: absolute; left: 150px; width: 580px; height: 100px; }
  .feature-one { top: 520px; }
  .feature-two { top: 642px; }
  .feature p {
    position: absolute; top: -2px; width: 370px; text-align: center;
    font-size: 11px; line-height: 18px; color: var(--ink);
  }
  .feature-one p { left: 0; }
  .feature-two p { left: 210px; }
  .video-thumb { position: absolute; top: 0; width: 200px; height: 100px; display: block; }
  .feature-one .video-thumb { left: 380px; }
  .feature-two .video-thumb { left: 0; }
  .feature-divider {
    position: absolute; left: 150px; top: 630px; width: 580px; height: 2px;
    border-top: 1px solid var(--rule); border-bottom: 1px solid #fafafa;
  }

  /* Sidebar */
  .social-bar {
    position: absolute; left: 750px; top: 470px; width: 300px; height: 35px;
    border: 1px solid var(--panel-border);
    background: linear-gradient(#f7f7f7, #ebebeb);
  }
  .social-bar h2 { position: absolute; left: 10px; top: 11px; font-size: 12px; font-weight: 700; }
  .social-link { position: absolute; top: 5px; width: 25px; height: 25px; border-radius: 3px; }
  .social-link.one { left: 237px; background: #7dcbe6; }
  .social-link.two { left: 268px; background: #3f62a8; }

  .news-panel {
    position: absolute; left: 750px; top: 515px; width: 300px; height: 330px;
    border: 1px solid var(--panel-border);
    background: linear-gradient(#f4f4f4, #e9e9e9);
    box-shadow: 0 0 3px rgba(0,0,0,0.12);
  }
  .news-panel h2 {
    position: absolute; left: 10px; top: 10px; width: 280px; padding-bottom: 7px;
    border-bottom: 1px solid var(--rule);
    font-size: 13px; font-weight: 700; color: var(--ink);
  }
  .news-item { position: absolute; left: 10px; width: 285px; height: 80px; }
  .news-item:nth-of-type(1) { top: 41px; }
  .news-item:nth-of-type(2) { top: 141px; }
  .news-item:nth-of-type(3) { top: 241px; }
  .news-thumb {
    position: absolute; left: 0; top: 0; width: 80px; height: 80px;
    background: linear-gradient(160deg, var(--thumb-light) 0%, #c3cdd1 45%, var(--thumb-blue) 100%);
  }
  .news-item h3 {
    position: absolute; left: 90px; top: -2px; width: 195px;
    font-size: 12px; line-height: 19px; font-weight: 700; color: var(--ink);
  }
  .read-more {
    position: absolute; left: 90px; top: 59px;
    font-size: 11px; font-style: italic; color: var(--ink); text-decoration: none;
  }
  .more-news {
    position: absolute; left: 761px; top: 851px;
    font-size: 12px; font-weight: 700; font-style: italic; color: var(--ink); text-decoration: none;
  }

  /* Footer */
  .site-footer {
    position: absolute; left: 0; top: 888px; width: 1200px; height: 152px;
    border-top: 1px solid #cfcfcf;
    background: linear-gradient(#fbfbf9, #f0f0ee 60%, #e9e9e7);
    text-align: center; font-size: 11px; color: var(--ink);
  }
  .site-footer .copyright { position: absolute; left: 0; top: 11px; width: 1200px; }
  .site-footer .footer-note { position: absolute; left: 0; top: 47px; width: 1200px; }
</style>
</head>
<body>
  <header class="site-header">
    <div class="brand"><span class="brand-dot"></span><span>Vantorell</span></div>
    <nav class="main-nav">
      <a href="#" class="is-active">Home</a>
      <a href="#">About Us</a>
      <a href="#">Technology</a>
      <a href="#">Press</a>
      <a href="#">Contact Us</a>
    </nav>
  </header>

  <div class="hero" role="img" aria-label="Illustration of a video analytics dashboard with charts, a question mark and a row of video players"></div>

  <main>
    <h1 class="welcome-title">Welcome to Vantorell!</h1>

    <section class="feature feature-one">
      <p>Lorem ipsum dolor sit amet, consectetur adipiscing elit. Vestibulum in consequat lorem. Nam adipiscing convallis elit, porttitor volutpat sem suscipit at. Mauris vel nunc ligula, gravida convallis metus. Cras sit amet quam justo. Donec blandit lorem vel risus volutpat eleifend nec sit amet odio. Suspendisse euismod dignissim nulla. In a odio diam, tempus commodo</p>
      <svg class="video-thumb" viewBox="0 0 200 100" role="img" aria-label="Video player">
        <defs>
          <radialGradient id="vidA" cx="50%" cy="40%" r="70%">
            <stop offset="0" stop-color="#2f95e6"/><stop offset="1" stop-color="#0546ae"/>
          </radialGradient>
        </defs>
        <rect width="200" height="100" fill="url(#vidA)"/>
        <circle cx="100" cy="45" r="27" fill="none" stroke="#fff" stroke-width="6" opacity="0.85"/>
        <path d="M93 31 L115 45 L93 59 Z" fill="#fff" opacity="0.9"/>
      </svg>
    </section>

    <div class="feature-divider"></div>

    <section class="feature feature-two">
      <svg class="video-thumb" viewBox="0 0 200 100" role="img" aria-label="Video player">
        <defs>
          <radialGradient id="vidB" cx="50%" cy="40%" r="70%">
            <stop offset="0" stop-color="#2f95e6"/><stop offset="1" stop-color="#0546ae"/>
          </radialGradient>
        </defs>
        <rect width="200" height="100" fill="url(#vidB)"/>
        <circle cx="100" cy="45" r="27" fill="none" stroke="#fff" stroke-width="6" opacity="0.85"/>
        <path d="M93 31 L115 45 L93 59 Z" fill="#fff" opacity="0.9"/>
      </svg>
      <p>Lorem ipsum dolor sit amet, consectetur adipiscing elit. Vestibulum in consequat lorem. Nam adipiscing convallis elit, porttitor volutpat sem suscipit at. Mauris vel nunc ligula, gravida convallis metus. Cras sit amet quam justo. Donec blandit lorem vel risus volutpat eleifend nec sit amet odio. Suspendisse euismod dignissim nulla. In a odio diam, tempus commodo</p>
    </section>
  </main>

  <aside>
    <div class="social-bar">
      <h2>Follow us on social networks!</h2>
      <a href="#" class="social-link one" aria-label="Follow us on our microblog"></a>
      <a href="#" class="social-link two" aria-label="Follow us on our social page"></a>
    </div>

    <section class="news-panel">
      <h2>Latest news!</h2>
      <article class="news-item">
        <div class="news-thumb" role="img" aria-label="Report chart preview"></div>
        <h3>Vestibulum in consequat lorem. Nam adipiscing convallis elit, porttitor volutpat sem suscipit at.</h3>
        <a href="#" class="read-more">Read more...</a>
      </article>
      <article class="news-item">
        <div class="news-thumb" role="img" aria-label="Report chart preview"></div>
        <h3>Vestibulum in consequat lorem. Nam adipiscing convallis elit, porttitor volutpat sem suscipit at.</h3>
        <a href="#" class="read-more">Read more...</a>
      </article>
      <article class="news-item">
        <div class="news-thumb" role="img" aria-label="Report chart preview"></div>
        <h3>Vestibulum in consequat lorem. Nam adipiscing convallis elit, porttitor volutpat sem suscipit at.</h3>
        <a href="#" class="read-more">Read more...</a>
      </article>
    </section>
    <a href="#" class="more-news">More news...</a>
  </aside>

  <footer class="site-footer">
    <p class="copyright">Copyright 2012 Oskar Lindvee &nbsp;|&nbsp; Remove this notice when you choose and get this design</p>
    <p class="footer-note">This is the footer part - add anything that you want here</p>
  </footer>
</body>
</html>
```